Real Estate Wordpress Landing Page

I'm looking to a landing page dedicated to my real estate brokerage that's catered to promoting that my company provides 1.5% listings to home sellers... I have a couple examples that I'm really looking towards mocking in a version with similar color schemes using my current company colors/website.

http://lorvanta.com/
https://www.bluthorn.com/about/one-percent-listing-fee

My brokerage company website is http://www.calmridge.us/

Target Market(s)

real estate home sellers & buyers

Industry/Entity Type

Real Estate

Coding

Coded - Design and coding required

Number of Pages Required

1 page

Colors
3176b5
0255a3
eaf1f7
cedeed

Requirements
Must have
• Company website colors - http://www.calmridge.us/
• Something around the lines of this website page - http://lorvanta.com/
• Wordpress compatibility

```html
<!DOCTYPE html>
<html lang="en">
<head>
<meta charset="utf-8">
<title>Calm Ridge – List For 1.5% Commission</title>
<link href="https://fonts.googleapis.com/css2?family=Kaushan+Script&family=Montserrat:wght@400;500;600;700;800&family=Open+Sans:wght@400;600;700&display=swap" rel="stylesheet">
<style>
:root{
  --blue:#3176b5;
  --blue-deep:#0255a3;
  --indigo:#3a4f9f;
  --navy:#1d2235;
  --navy-2:#262c42;
  --ice:#eaf1f7;
  --mist:#cedeed;
  --grey-bg:#eeeff2;
  --text:#4a4f5c;
  --muted:#8a8f9a;
  --white:#ffffff;
}
*{box-sizing:border-box;margin:0;padding:0}
html,body{width:1200px;height:5099px;overflow:hidden}
body{font-family:"Open Sans",Arial,sans-serif;color:var(--text);background:var(--white);position:relative;font-size:13px}
section,header,footer{position:absolute;left:0;width:1200px}
.abs{position:absolute}
.script{font-family:"Kaushan Script",cursive;font-weight:400}
.sec-title{position:absolute;left:0;width:1200px;text-align:center;font-family:"Kaushan Script",cursive;color:var(--blue-deep);font-size:36px}
.btn{display:inline-block;background:var(--navy);color:var(--white);font-family:Montserrat,sans-serif;font-weight:700;font-size:11px;letter-spacing:.5px;padding:10px 22px;border-radius:20px;text-transform:uppercase}
.ph{background:linear-gradient(160deg,#9fb6cc,#5d7389 60%,#3e4d5c)}
.ph-green{background:linear-gradient(180deg,#a9c4df 0%,#d9dcd3 45%,#7e9a62 100%)}
.ph-room{background:linear-gradient(160deg,#e4e2de,#a9a5a0 70%,#6e6a66)}

/* header */
.site-header{top:0;height:118px;background:var(--white);z-index:3}
.topbar{position:absolute;right:40px;top:8px;display:flex;gap:14px;font-size:11px;color:var(--text)}
.topbar span{display:flex;align-items:center;gap:6px}
.brand{position:absolute;left:225px;top:20px;display:flex;align-items:center;gap:10px;font-family:Montserrat,sans-serif;font-weight:800;color:var(--blue-deep);font-size:22px}
.brand i{width:26px;height:26px;background:var(--blue-deep);display:block}
.nav{position:absolute;left:440px;top:52px;display:flex;gap:26px;font-family:Montserrat,sans-serif;font-size:11px;font-weight:600;color:var(--text);text-transform:uppercase}
.auth{position:absolute;left:812px;top:46px;display:flex;gap:10px}
.auth span{font-size:11px;font-family:Montserrat,sans-serif;font-weight:600;padding:6px 18px;border-radius:14px;border:1px solid var(--blue-deep);color:var(--blue-deep)}
.auth span.fill{background:var(--blue-deep);color:var(--white)}

/* hero */
.hero{top:118px;height:494px}
.hero-photo{position:absolute;inset:0;background:linear-gradient(180deg,#2b3550 0%,#4a5670 45%,#6c6a5c 80%,#3d4a2f 100%)}
.hero-box{position:absolute;left:204px;top:88px;width:496px;padding:22px 26px;background:rgba(49,70,150,.85)}
.hero-box h1{font-family:"Kaushan Script",cursive;font-weight:400;color:var(--white);font-size:42px;line-height:1.1}
.hero-box p{color:var(--white);font-family:Montserrat,sans-serif;font-weight:700;font-size:13px;text-transform:uppercase;margin-top:6px}
.hero .btn{position:absolute;left:204px;top:258px}

/* sold grid */
.sold{top:612px;height:628px;background:var(--white)}
.sold .sec-title{top:60px}
.grid{position:absolute;left:211px;top:128px;display:grid;grid-template-columns:repeat(3,245px);column-gap:24px;row-gap:26px}
.card{background:var(--white);box-shadow:0 2px 8px rgba(0,0,0,.12);height:220px}
.card .img{height:152px;position:relative}
.price{position:absolute;left:0;bottom:0;background:var(--navy);color:var(--white);font-family:Montserrat,sans-serif;font-weight:700;font-size:11px;padding:4px 10px}
.card .addr{font-family:Montserrat,sans-serif;font-size:11px;font-weight:600;color:var(--blue-deep);padding:10px 10px 4px}
.card .specs{font-size:10px;color:var(--muted);padding:0 10px}

/* dark band */
.band{top:1240px;height:545px;background:var(--navy)}
.band h2{position:absolute;top:72px;width:1200px;text-align:center;font-family:"Kaushan Script",cursive;font-weight:400;color:var(--white);font-size:36px;line-height:1.05}
.band h2 small{display:block;font-size:22px}
.band-cards{position:absolute;left:211px;top:204px;display:flex;gap:22px}
.bcard{width:248px;height:238px;background:var(--white);overflow:hidden;position:relative}
.bcard .img{height:168px}
.ribbon{position:absolute;right:-30px;top:18px;width:130px;transform:rotate(45deg);background:var(--blue-deep);color:var(--white);text-align:center;font-family:Montserrat,sans-serif;font-weight:700;font-size:10px;padding:3px 0}
.bcard .addr{font-family:Montserrat,sans-serif;font-size:11px;font-weight:600;color:var(--blue-deep);padding:10px 10px 3px}
.bcard .specs{font-size:10px;color:var(--muted);padding:0 10px}
.arrow{position:absolute;width:26px;height:26px;border-radius:50%;border:1px solid rgba(255,255,255,.4)}
.band .btn{position:absolute;left:540px;top:468px;background:var(--indigo)}

/* broker */
.broker{top:1785px;height:323px;background:var(--white)}
.broker h3{position:absolute;left:211px;top:45px;font-family:"Kaushan Script",cursive;font-weight:400;color:var(--blue-deep);font-size:26px}
.broker .bio{position:absolute;left:211px;top:95px;width:460px;font-size:11px;line-height:1.6}
.broker .call{position:absolute;left:211px;top:150px;font-family:Montserrat,sans-serif;font-weight:700;font-size:10px;color:var(--navy)}
.broker .phone{position:absolute;left:211px;top:168px;display:flex;align-items:center;gap:8px;font-family:Montserrat,sans-serif;font-weight:700;color:var(--blue-deep);font-size:20px}
.broker .site{position:absolute;left:211px;top:204px;font-size:11px}
.socials{display:flex;gap:6px}
.socials i{width:18px;height:18px;border-radius:50%;background:#a12c3a;display:block}
.broker .socials{position:absolute;left:211px;top:226px}
.portrait{position:absolute;left:731px;top:45px;width:364px;height:252px;background:linear-gradient(180deg,#c9ccd1,#8d929b)}

/* savings */
.savings{top:2108px;height:612px;background:var(--grey-bg)}
.savings .sec-title{top:80px}
.savings .caption{position:absolute;top:172px;width:1200px;text-align:center;font-family:Montserrat,sans-serif;font-weight:700;color:var(--navy);font-size:14px}
.chip{position:absolute;background:var(--white);box-shadow:0 1px 4px rgba(0,0,0,.12);padding:8px 12px;text-align:center;width:150px}
.chip b{display:block;font-family:Montserrat,sans-serif;color:var(--blue-deep);font-size:15px}
.chip span{font-size:10px;color:var(--text)}
.savings .total{position:absolute;top:490px;width:1200px;text-align:center;font-family:Montserrat,sans-serif;font-weight:800;color:var(--navy);font-size:20px}
.savings .total em{font-style:normal;color:var(--blue-deep)}
.savings .btn{position:absolute;left:520px;top:555px}

/* services */
.services{top:2720px;height:1088px;background:var(--white)}
.services .sec-title{top:90px;font-size:30px}
.services .sub{position:absolute;top:138px;width:1200px;text-align:center;font-family:Montserrat,sans-serif;font-weight:600;font-size:12px;color:var(--navy);text-transform:uppercase}
.svc{position:absolute;width:760px;height:280px}
.svc .img{position:absolute;width:238px;height:170px}
.svc .cap{position:absolute;font-family:Montserrat,sans-serif;font-size:11px;font-weight:600;color:var(--blue-deep)}
.svc .txt{position:absolute;width:430px}
.svc h4{font-family:Montserrat,sans-serif;font-weight:500;color:var(--blue-deep);font-size:20px;text-transform:uppercase;margin-bottom:12px}
.svc ul{list-style:none;font-size:11px;margin-bottom:10px}
.svc li{display:flex;gap:8px;align-items:center;margin-bottom:6px}
.svc li i{width:11px;height:11px;border:1px solid var(--blue);display:block}
.svc p{font-size:11px;line-height:1.6;margin-bottom:12px}

/* testimonials */
.testimonials{top:3808px;height:340px;background:var(--indigo)}
.testimonials .sec-title{top:40px;color:var(--white)}
.tcard{position:absolute;top:120px;width:360px;height:120px;background:var(--white);padding:18px;font-size:10px;line-height:1.6}
.tcard .who{margin-top:10px;font-family:Montserrat,sans-serif;font-weight:600;color:var(--blue-deep)}
.avatar{position:absolute;width:70px;height:70px;border-radius:50%;background:var(--mist);border:3px solid var(--white)}

/* blog */
.blog{top:4148px;height:442px;background:var(--white)}
.blog .sec-title{top:44px}
.post{position:absolute;top:118px;width:420px;height:200px}
.post .img{position:absolute;left:0;top:0;width:180px;height:200px}
.post h5{position:absolute;left:200px;top:6px;width:220px;font-family:Montserrat,sans-serif;font-weight:700;color:var(--navy);font-size:13px;line-height:1.35}
.post p{position:absolute;left:200px;top:58px;width:215px;font-size:10px;line-height:1.6}
.post .more{position:absolute;left:200px;top:176px;font-family:Montserrat,sans-serif;font-weight:700;font-size:10px;color:var(--blue-deep)}
.blog .btn{position:absolute;left:552px;top:372px}

/* partners */
.partners{top:4590px;height:136px;background:var(--white);border-top:1px solid var(--mist)}
.partner{position:absolute;top:40px;width:130px;height:56px;background:var(--ice);border-radius:4px}

/* footer */
.site-footer{top:4726px;height:373px;background:var(--navy)}
.foot-left{position:absolute;left:0;top:0;width:560px;height:318px;background:var(--indigo);clip-path:polygon(0 0,100% 0,80% 100%,0 100%)}
.site-footer h6{position:absolute;font-family:"Kaushan Script",cursive;font-weight:400;color:var(--white);font-size:28px}
.contact-list{position:absolute;left:211px;top:92px;list-style:none;color:var(--white);font-size:11px}
.contact-list li{display:flex;gap:10px;align-items:flex-start;margin-bottom:14px;line-height:1.4}
.contact-list li i{width:22px;height:22px;border-radius:50%;background:rgba(255,255,255,.18);display:flex;align-items:center;justify-content:center;flex:none}
.form{position:absolute;left:500px;top:30px;width:490px}
.field{height:28px;background:var(--navy-2);border:1px solid #3a4160;margin-bottom:10px;color:#9aa0b4;font-size:10px;padding:7px 10px}
.form .row{display:flex;gap:10px}
.form .row .field{flex:1}
.form .area{height:66px}
.form .btn{background:var(--indigo);border-radius:2px;padding:8px 18px}
.bottom{position:absolute;left:0;top:318px;width:1200px;height:55px;background:#161a29;border-top:1px solid #2f3552}
.bottom span{position:absolute;left:211px;top:20px;font-size:10px;color:#8a90a6}
.bottom .socials{position:absolute;left:820px;top:18px}
.bottom .socials i{background:transparent;border:1px solid #8a90a6}
</style>
</head>
<body>

<header class="site-header">
  <div class="topbar">
    <span><svg width="10" height="10" viewBox="0 0 10 10"><path d="M2 1l2 2-1 1c1 1 2 2 3 3l1-1 2 2-1 1.5C5 9 1 5 .5 2z" fill="#3176b5"/></svg>555-014-2290</span>
    <span><svg width="11" height="9" viewBox="0 0 11 9"><rect x=".5" y=".5" width="10" height="8" fill="none" stroke="#3176b5"/><path d="M.5 .5l5 4 5-4" fill="none" stroke="#3176b5"/></svg>hello@calmridge.us</span>
  </div>
  <div class="brand"><i></i>Calm Ridge</div>
  <nav class="nav"><span>Buy With Us ▾</span><span>Sell With Us ▾</span><span>Real Estate Agents</span></nav>
  <div class="auth"><span class="fill">Log In</span><span>Sign Up</span></div>
</header>

<section class="hero">
  <div class="hero-photo" role="img" aria-label="Two-storey suburban home at dusk with a for-sale sign on the lawn"></div>
  <div class="hero-box">
    <h1>List For 1.5% Commission</h1>
    <p>And receive top marketing from real estate pro!</p>
  </div>
  <span class="btn">Contact Us Today</span>
</section>

<section class="sold">
  <h2 class="sec-title">Latest Properties We've Sold</h2>
  <div class="grid">
    <div class="card"><div class="img ph-green" role="img" aria-label="Sold single-family home"><span class="price">$390,000</span></div><div class="addr">8624 NW 9th Street, Harbor Vale...</div><div class="specs">3 bd · 2 ba · 1,870 sq ft</div></div>
    <div class="card"><div class="img ph-green" role="img" aria-label="Sold ranch-style home"><span class="price">$355,000</span></div><div class="addr">1024 Elm Parkside Circle, Cedar Point</div><div class="specs">3 bd · 2 ba · 1,540 sq ft</div></div>
    <div class="card"><div class="img ph-green" role="img" aria-label="Sold townhouse"><span class="price">$280,000</span></div><div class="addr">4503 NW 5th Street, Harbor Vale...</div><div class="specs">2 bd · 2 ba · 1,210 sq ft</div></div>
    <div class="card"><div class="img ph-green" role="img" aria-label="Sold two-storey home with palms"><span class="price">$415,000</span></div><div class="addr">9265 Redwood Cove Lane, Cedar...</div><div class="specs">4 bd · 3 ba · 2,330 sq ft</div></div>
    <div class="card"><div class="img ph-green" role="img" aria-label="Sold home with garage"><span class="price">$342,000</span></div><div class="addr">9063 Pondside Lane, Cedar Point</div><div class="specs">3 bd · 2 ba · 1,690 sq ft</div></div>
    <div class="card"><div class="img ph-green" role="img" aria-label="Sold home with tiled roof"><span class="price">$305,000</span></div><div class="addr">6372 Bay Harbor Lane, Harbor Vale</div><div class="specs">3 bd · 2 ba · 1,480 sq ft</div></div>
  </div>
</section>

<section class="band">
  <h2>List For 1.5% Commission,<small>And Receive Top Marketing From Real Estate Pro!</small></h2>
  <span class="arrow" style="left:160px;top:308px"></span>
  <span class="arrow" style="left:1014px;top:308px"></span>
  <div class="band-cards">
    <div class="bcard"><div class="img ph-green" role="img" aria-label="Listed home exterior"></div><span class="ribbon">Just Sold</span><div class="addr">9265 Redwood Cove Lane, Cedar Point</div><div class="specs">$415,000 · 4 bd · 3 ba</div></div>
    <div class="bcard"><div class="img ph-room" role="img" aria-label="Bright living room interior"></div><span class="ribbon">Just Sold</span><div class="addr">4420 Fairhaven Boulevard, Harbor Vale</div><div class="specs">$298,000 · 2 bd · 2 ba</div></div>
    <div class="bcard"><div class="img ph-green" role="img" aria-label="Home with palm trees"></div><span class="ribbon">Just Sold</span><div class="addr">1024 Elm Parkside Circle, Cedar Point</div><div class="specs">$355,000 · 3 bd · 2 ba</div></div>
  </div>
  <span class="btn">View All</span>
</section>

<section class="broker">
  <h3>Marcus Ellery, Lic. Real Estate Broker</h3>
  <p class="bio">On average, our customers save $9,600 when they list with us – and they still receive top marketing and quality professional service.</p>
  <div class="call">CALL OR TEXT ANYTIME</div>
  <div class="phone"><svg width="20" height="20" viewBox="0 0 20 20"><circle cx="10" cy="10" r="10" fill="#0255a3"/><path d="M7 5l2 2-1 1.2c.8 1.5 1.9 2.6 3.3 3.3l1.2-1 2 2-1.3 1.6C9.8 14 6 10.2 5.5 6.3z" fill="#fff"/></svg>555-014-2290</div>
  <div class="site">www.calmridge.us</div>
  <div class="socials"><i></i><i></i><i></i><i></i><i></i><i></i></div>
  <div class="portrait" role="img" aria-label="Portrait of the broker in a dark suit"></div>
</section>

<section class="savings">
  <h2 class="sec-title">See how much you could save with Calm Ridge</h2>
  <div class="caption">Our Client Savings</div>
  <svg class="abs" style="left:458px;top:200px" width="280" height="280" viewBox="0 0 280 280" role="img" aria-label="Pie chart comparing commission costs">
    <circle cx="140" cy="140" r="136" fill="#3a4f9f"/>
    <path d="M140 140 L140 4 A136 136 0 0 1 276 140 Z" fill="#3176b5"/>
    <path d="M140 140 L276 140 A136 136 0 0 1 240 232 Z" fill="#cedeed"/>
    <circle cx="140" cy="140" r="46" fill="#fff"/>
    <text x="140" y="145" text-anchor="middle" font-family="Montserrat,sans-serif" font-weight="800" font-size="14" fill="#0255a3">Calm Ridge</text>
  </svg>
  <div class="chip" style="left:262px;top:222px"><b>$5,775</b><span>Calm Ridge Listing Rate</span></div>
  <div class="chip" style="left:790px;top:222px"><b>$1,850</b><span>Calm Ridge Buyer Rebate</span></div>
  <div class="chip" style="left:262px;top:398px"><b>$11,550</b><span>Traditional Listing Rate</span></div>
  <div class="chip" style="left:790px;top:398px"><b>$0</b><span>Traditional Brokerage Rebate</span></div>
  <div class="abs" style="left:640px;top:232px;font-family:Montserrat,sans-serif;font-weight:700;font-size:11px;color:#fff">$250,000</div>
  <div class="abs" style="left:0;width:1200px;text-align:center;top:465px;font-family:Montserrat,sans-serif;font-size:12px;color:#1d2235">Traditional Brokerage</div>
  <div class="total">TOTAL SAVINGS WHEN YOU USE US: <em>$9,625</em></div>
  <span class="btn">Contact Us Today</span>
</section>

<section class="services">
  <h2 class="sec-title">30 Day Listing Service Guaranteed. Save Thousands $$$ Listing With Us!</h2>
  <div class="sub">Morbi eu sem felis. Integer faucibus ligula vitae enim vestibulum auctor.</div>

  <div class="svc" style="left:238px;top:200px">
    <div class="img ph-green" style="left:0;top:10px" role="img" aria-label="Home listed for sale"></div>
    <div class="cap" style="left:0;top:192px">1275 Country Club Drive, Harbor Vale<br>FL 33436 · $389,000</div>
    <div class="txt" style="left:306px;top:0">
      <h4>Sell With Calm Ridge &amp; Save $$$</h4>
      <ul><li><i></i>Professional Real Estate Photography</li><li><i></i>Comprehensive Comparative Market Analysis (CMA)</li><li><i></i>FREE Consultation with Real Estate Professional</li></ul>
      <p>Lorem ipsum dolor sit amet, consectetuer adipiscing elit, sed diam nonummy nibh euismod tincidunt ut laoreet dolore magna aliquam erat volutpat. Ut wisi enim ad minim veniam.</p>
      <span class="btn">☎ 555-014-2290</span>
    </div>
  </div>

  <div class="svc" style="left:238px;top:476px">
    <div class="txt" style="left:0;top:0">
      <h4>Start Your Home Search With Us</h4>
      <ul><li><i></i>1% Buyer Credit at Closing from Calm Ridge</li><li><i></i>Quis Molestie Turpis Dapibus At</li><li><i></i>Quis Molestie Turpis Dapibus At</li></ul>
      <p>Lorem ipsum dolor sit amet, consectetuer adipiscing elit, sed diam nonummy nibh euismod tincidunt ut laoreet dolore magna aliquam erat volutpat. Ut wisi enim ad minim veniam.</p>
      <span class="btn">☎ 555-014-2290</span>
    </div>
    <div class="img ph-room" style="left:508px;top:10px;overflow:hidden" role="img" aria-label="Modern living room"><span class="ribbon" style="top:16px">For Sale</span></div>
    <div class="cap" style="left:508px;top:192px">1275 Country Club Drive, Harbor Vale<br>FL 33436 · $389,000</div>
  </div>

  <div class="svc" style="left:238px;top:782px">
    <div class="img ph-green" style="left:0;top:10px" role="img" aria-label="Rental home exterior"></div>
    <div class="cap" style="left:0;top:192px">1275 Country Club Drive, Harbor Vale<br>FL 33436 · $389,000</div>
    <div class="txt" style="left:306px;top:0">
      <h4>Leasing &amp; Property Management</h4>
      <ul><li><i></i>We can manage your rental portfolio for you</li><li><i></i>Professional &amp; Experienced Property Managers</li><li><i></i>Receive Top Dollar for your Rental Properties</li></ul>
      <p>Lorem ipsum dolor sit amet, consectetuer adipiscing elit, sed diam nonummy nibh euismod tincidunt ut laoreet dolore magna aliquam erat volutpat.</p>
      <span class="btn">☎ 555-014-2290</span>
    </div>
  </div>
</section>

<section class="testimonials">
  <h2 class="sec-title">Client Testimonials</h2>
  <span class="arrow" style="left:160px;top:172px"></span>
  <span class="arrow" style="left:1014px;top:172px"></span>
  <div class="tcard" style="left:211px">Lorem ipsum dolor sit amet, consectetuer adipiscing elit, sed diam nonummy nibh euismod tincidunt ut laoreet dolore magna aliquam erat volutpat.<div class="who">Lena Marsh ★★★★★</div></div>
  <div class="avatar" style="left:470px;top:210px" role="img" aria-label="Client photo"></div>
  <div class="tcard" style="left:630px">Lorem ipsum dolor sit amet, consectetuer adipiscing elit, sed diam nonummy nibh euismod tincidunt ut laoreet dolore magna aliquam erat volutpat.<div class="who">Wes Corbin ★★★★★</div></div>
  <div class="avatar" style="left:890px;top:210px" role="img" aria-label="Client photo"></div>
</section>

<section class="blog">
  <h2 class="sec-title">Latest Blog</h2>
  <span class="arrow" style="left:160px;top:200px;border-color:#cedeed"></span>
  <span class="arrow" style="left:1014px;top:200px;border-color:#cedeed"></span>
  <article class="post" style="left:211px">
    <div class="img" style="background:linear-gradient(180deg,#9cc6e6,#3aa0c4 55%,#e0d6c0)" role="img" aria-label="Coastal city skyline by the beach"></div>
    <h5>Skills That You Can Learn In The Real Estate Market</h5>
    <p>At vero eos et accusamus et iusto odio dignissimos ducimus qui blanditiis praesentium voluptatum deleniti atque corrupti quos dolores.</p>
    <span class="more">READ MORE</span>
  </article>
  <article class="post" style="left:650px">
    <div class="img" style="background:linear-gradient(180deg,#7fb0e0,#e8e6e0 60%,#6b8a52)" role="img" aria-label="White villa with tiled roof"></div>
    <h5>Learn The Truth About Real Estate Industry</h5>
    <p>At vero eos et accusamus et iusto odio dignissimos ducimus qui blanditiis praesentium voluptatum deleniti atque corrupti quos dolores.</p>
    <span class="more">READ MORE</span>
  </article>
  <span class="btn">View All</span>
</section>

<section class="partners">
  <div class="partner" style="left:211px"></div>
  <div class="partner" style="left:430px"></div>
  <div class="partner" style="left:650px"></div>
  <div class="partner" style="left:864px"></div>
</section>

<footer class="site-footer">
  <div class="foot-left"></div>
  <h6 style="left:211px;top:36px">Get In Touch</h6>
  <ul class="contact-list">
    <li><i><svg width="10" height="12" viewBox="0 0 10 12"><path d="M5 0a4 4 0 0 1 4 4c0 3-4 8-4 8S1 7 1 4a4 4 0 0 1 4-4z" fill="#fff"/></svg></i><span>Marcus Ellery<br>7620 Harbor Vale Road, Unit 12<br>Harbor Vale, FL 33400</span></li>
    <li><i><svg width="11" height="9" viewBox="0 0 11 9"><rect x=".5" y=".5" width="10" height="8" fill="none" stroke="#fff"/><path d="M.5 .5l5 4 5-4" fill="none" stroke="#fff"/></svg></i><span>hello@calmridge.us</span></li>
    <li><i><svg width="10" height="10" viewBox="0 0 10 10"><path d="M2 1l2 2-1 1c1 1 2 2 3 3l1-1 2 2-1 1.5C5 9 1 5 .5 2z" fill="#fff"/></svg></i><span>555-014-2290</span></li>
    <li><i><svg width="10" height="10" viewBox="0 0 10 10"><path d="M2 1l2 2-1 1c1 1 2 2 3 3l1-1 2 2-1 1.5C5 9 1 5 .5 2z" fill="#fff"/></svg></i><span>555-014-2291</span></li>
  </ul>
  <h6 style="left:640px;top:36px">Quick Contact</h6>
  <div class="form" style="top:92px">
    <div class="row"><div class="field">Name</div><div class="field">Email</div></div>
    <div class="row"><div class="field">Phone</div><div class="field">Subject</div></div>
    <div class="field area">Message</div>
    <span class="btn">Submit Now</span>
  </div>
  <div class="bottom">
    <span>© 2024 Calm Ridge. All rights reserved.</span>
    <div class="socials"><i></i><i></i><i></i><i></i><i></i><i></i></div>
  </div>
</footer>

</body>
</html>
```